Flyer for the Lumen 2025 Conference

I am looking to produce a flyer for our upcoming conference, Lumen 2025. This is an annual conference that we plan to publicize on social media. The ideal designer will create a flyer that is eye-catching and effectively communicates the key information. Please see attached our logo, speaker photo, and flyer content.

Target Market(s)

All demographics

Industry/Entity Type

Christian

Font styles to use
Sans Serif

Requirements
Should not have
• Cross, church

```html
<!DOCTYPE html>
<html lang="en">
<head>
<meta charset="utf-8">
<title>Lumen 2025 Conference Flyer</title>
<link href="https://fonts.googleapis.com/css2?family=Montserrat:wght@400;500;600;700;800;900&family=Kaushan+Script&display=swap" rel="stylesheet">
<style>
  :root {
    --pink: #e46ad8;
    --violet: #8a2fbf;
    --purple: #6a27a8;
    --indigo: #3b2a8a;
    --navy: #1c2a5c;
    --band: #0e3358;
    --orange: #f47a1f;
    --amber: #ffb01a;
    --yellow: #ffc914;
    --white: #ffffff;
    --ink: #111111;
    --photo-blue: #1e67b5;
  }
  * { margin: 0; padding: 0; box-sizing: border-box; }
  html, body { width: 848px; height: 1200px; overflow: hidden; background: var(--navy); }
  .flyer {
    position: relative; width: 848px; height: 1200px; overflow: hidden;
    font-family: "Montserrat", sans-serif; color: var(--white);
    background: linear-gradient(180deg, var(--pink) 0%, #c75bd6 22%, var(--violet) 42%, var(--purple) 55%, var(--indigo) 75%, var(--navy) 100%);
  }
  .sky-glow {
    position: absolute; left: 0; top: 0; width: 848px; height: 520px;
    background: radial-gradient(ellipse at 30% 20%, rgba(255,180,240,.55), transparent 60%);
  }
  .brand-band {
    position: absolute; left: 269px; top: 0; width: 310px; height: 280px;
    background: linear-gradient(180deg, var(--band) 0%, rgba(14,51,88,.85) 45%, rgba(14,51,88,0) 100%);
  }
  .brand {
    position: absolute; left: 288px; top: 112px; display: flex; align-items: center; gap: 12px;
  }
  .brand-dot { width: 34px; height: 34px; border-radius: 50%; background: var(--orange); }
  .brand-name { font-weight: 600; font-size: 62px; letter-spacing: 2px; color: var(--white); line-height: 1; }
  .dove-art {
    position: absolute; left: 580px; top: 0; width: 268px; height: 240px;
    background: radial-gradient(ellipse at 55% 45%, rgba(255,230,255,.75), rgba(240,150,220,.35) 50%, transparent 75%);
  }
  .title {
    position: absolute; left: 108px; top: 250px; transform: rotate(-7deg); transform-origin: left center;
  }
  .title-word {
    font-weight: 900; font-size: 150px; line-height: 1; letter-spacing: 2px;
    background: linear-gradient(180deg, #ffd54a 0%, var(--amber) 45%, var(--orange) 100%);
    -webkit-background-clip: text; background-clip: text; color: transparent;
    filter: drop-shadow(4px 6px 0 #c2410c) drop-shadow(2px 8px 6px rgba(60,0,60,.5));
  }
  .title-year {
    position: absolute; left: 662px; top: 36px; font-weight: 900; font-size: 34px; line-height: .9; color: var(--white);
  }
  .subtitle {
    position: absolute; left: 150px; top: 410px; transform: rotate(-11deg);
    font-family: "Kaushan Script", cursive; font-size: 62px; color: var(--white);
    text-shadow: 2px 3px 4px rgba(40,0,60,.4);
  }
  .speaker-card {
    position: absolute; left: 0; top: 554px; width: 206px; height: 90px;
    background: var(--ink); border: 3px solid var(--white); border-left: none; border-radius: 0 0 40px 0;
  }
  .speaker-label {
    position: absolute; left: 48px; top: -20px; font-family: "Kaushan Script", cursive; font-size: 28px; color: var(--orange);
  }
  .speaker-title { position: absolute; left: 20px; top: 26px; font-weight: 800; font-size: 27px; letter-spacing: .5px; }
  .speaker-name { position: absolute; left: 20px; top: 58px; font-weight: 500; font-size: 18px; }
  .speaker-line { position: absolute; height: 1px; background: var(--orange); }
  .speaker-photo {
    position: absolute; left: 0; top: 663px; width: 430px; height: 537px;
    background: linear-gradient(180deg, rgba(120,80,60,0) 0%, var(--photo-blue) 35%, #0f3f80 100%);
    clip-path: polygon(38% 0, 62% 0, 66% 20%, 95% 40%, 100% 100%, 0 100%, 5% 40%, 34% 20%);
  }
  .topic-bubble {
    position: absolute; left: 481px; top: 537px; width: 190px; height: 52px;
    background: var(--white); border-radius: 26px;
    font-weight: 800; font-size: 40px; color: var(--orange); text-align: center; line-height: 52px;
  }
  .topic-bubble::after {
    content: ""; position: absolute; left: 84px; bottom: -18px;
    border-left: 12px solid transparent; border-right: 12px solid transparent; border-top: 20px solid var(--white);
  }
  .topic-text {
    position: absolute; left: 397px; top: 606px; font-weight: 800; color: var(--yellow); font-size: 32px; white-space: nowrap;
  }
  .topic-text small { font-size: 20px; }
  .session { position: absolute; display: flex; align-items: center; }
  .session-day { text-align: right; font-weight: 800; color: var(--amber); line-height: .95; padding-right: 5px; border-right: 1.5px solid var(--white); }
  .session-day b { display: block; font-size: 13.5px; }
  .session-day span { display: block; font-size: 8.5px; }
  .session-date { font-weight: 800; font-size: 44px; color: var(--amber); padding: 0 4px 0 6px; position: relative; line-height: 1; }
  .session-date sup { position: absolute; right: -8px; top: -4px; font-size: 7px; color: var(--white); }
  .session-year { font-weight: 800; font-size: 14px; line-height: .9; color: var(--amber); padding-left: 6px; margin-left: 8px; border-left: 1.5px solid var(--white); }
  .session-clock { margin-left: 6px; }
  .contact-box {
    position: absolute; left: 344px; top: 926px; width: 462px; height: 76px;
    border: 1.5px solid var(--white); border-radius: 8px;
  }
  .contact-note {
    position: absolute; left: 111px; top: -9px; width: 268px; height: 17px; border-radius: 9px;
    background: var(--yellow); color: var(--ink); font-weight: 800; font-size: 6.8px; text-align: center; line-height: 17px;
  }
  .contact-phone { position: absolute; left: 0; right: 0; top: 14px; text-align: center; font-weight: 700; font-size: 20px; }
  .contact-row { position: absolute; left: 9px; top: 40px; display: flex; align-items: center; gap: 6px; font-weight: 700; font-size: 19px; }
  .contact-row .gap { width: 14px; }
  .venue {
    position: absolute; left: 399px; top: 1071px; width: 449px; height: 60px;
    background: var(--yellow); border-radius: 30px 0 0 30px; color: var(--ink);
  }
  .venue-pin { position: absolute; left: 18px; top: 12px; }
  .venue-name { position: absolute; left: 51px; top: 15px; font-weight: 800; font-size: 15.5px; white-space: nowrap; }
  .venue-address { position: absolute; left: 51px; top: 35px; font-weight: 700; font-size: 13px; white-space: nowrap; }
</style>
</head>
<body>
<main class="flyer">
  <div class="sky-glow"></div>
  <div class="brand-band"></div>
  <div class="brand"><span class="brand-dot"></span><span class="brand-name">SOLARE</span></div>
  <div class="dove-art" role="img" aria-label="Soft illustration of a white dove rising from open hands"></div>

  <h1 class="title">
    <span class="title-word">LUMEN</span>
    <span class="title-year">20<br>25</span>
  </h1>
  <p class="subtitle">A Prophetic Conference</p>

  <div class="speaker-line" style="left:122px;top:540px;width:50px"></div>
  <div class="speaker-line" style="left:122px;top:546px;width:62px"></div>
  <section class="speaker-card">
    <span class="speaker-label">Speaker</span>
    <span class="speaker-title">PROPHET</span>
    <span class="speaker-name">SAMUEL OKORO</span>
  </section>
  <div class="speaker-line" style="left:0;top:648px;width:52px"></div>
  <div class="speaker-line" style="left:66px;top:648px;width:10px"></div>
  <div class="speaker-line" style="left:150px;top:648px;width:58px"></div>

  <div class="speaker-photo" role="img" aria-label="Photo of the speaker seated in a blue suit"></div>

  <div class="topic-bubble">TOPIC</div>
  <p class="topic-text"><small>THE </small>VOICE <small>OF THE </small>LORD</p>

  <div class="session" style="left:341px;top:715px">
    <div class="session-day"><b>FRIDAY</b><span>DECEMBER</span></div>
    <div class="session-date">26<sup>TH</sup></div>
    <div class="session-year">20<br>25</div>
    <svg class="session-clock" width="64" height="64" viewBox="0 0 64 64"><circle cx="32" cy="32" r="30" fill="none" stroke="#fff" stroke-width="3"/><g stroke="#fff" stroke-width="1"><line x1="32" y1="5" x2="32" y2="9"/><line x1="32" y1="55" x2="32" y2="59"/><line x1="5" y1="32" x2="9" y2="32"/><line x1="55" y1="32" x2="59" y2="32"/></g><g fill="#ffb01a" font-family="Montserrat, sans-serif" font-weight="800" text-anchor="middle"><text x="32" y="26" font-size="9">6:30</text><text x="32" y="44" font-size="9">9:00</text></g><g fill="#ffb01a" font-family="Montserrat, sans-serif" font-size="5" text-anchor="middle"><text x="32" y="32">PM</text><text x="32" y="50">PM</text></g></svg>
  </div>
  <div class="session" style="left:589px;top:715px">
    <div class="session-day"><b>SATURDAY</b><span>DECEMBER</span></div>
    <div class="session-date">27<sup>TH</sup></div>
    <div class="session-year">20<br>25</div>
    <svg class="session-clock" width="64" height="64" viewBox="0 0 64 64"><circle cx="32" cy="32" r="30" fill="none" stroke="#fff" stroke-width="3"/><g stroke="#fff" stroke-width="1"><line x1="32" y1="5" x2="32" y2="9"/><line x1="32" y1="55" x2="32" y2="59"/><line x1="5" y1="32" x2="9" y2="32"/><line x1="55" y1="32" x2="59" y2="32"/></g><g fill="#ffb01a" font-family="Montserrat, sans-serif" font-weight="800" text-anchor="middle"><text x="32" y="26" font-size="9">5:30</text><text x="32" y="44" font-size="9">8:00</text></g><g fill="#ffb01a" font-family="Montserrat, sans-serif" font-size="5" text-anchor="middle"><text x="32" y="32">PM</text><text x="32" y="50">PM</text></g></svg>
  </div>
  <div class="session" style="left:465px;top:785px">
    <div class="session-day"><b>SUNDAY</b><span>DECEMBER</span></div>
    <div class="session-date">29<sup>TH</sup></div>
    <div class="session-year">20<br>25</div>
    <svg class="session-clock" width="64" height="64" viewBox="0 0 64 64"><circle cx="32" cy="32" r="30" fill="none" stroke="#fff" stroke-width="3"/><g stroke="#fff" stroke-width="1"><line x1="32" y1="5" x2="32" y2="9"/><line x1="32" y1="55" x2="32" y2="59"/><line x1="5" y1="32" x2="9" y2="32"/><line x1="55" y1="32" x2="59" y2="32"/></g><g fill="#ffb01a" font-family="Montserrat, sans-serif" font-weight="800" text-anchor="middle"><text x="32" y="26" font-size="9">4:30</text><text x="32" y="44" font-size="9">7:00</text></g><g fill="#ffb01a" font-family="Montserrat, sans-serif" font-size="5" text-anchor="middle"><text x="32" y="32">PM</text><text x="32" y="50">PM</text></g></svg>
  </div>

  <section class="contact-box">
    <div class="contact-note">DOWNLOAD THE SOLARE APP TO STAY UPDATED ON THE EVENT</div>
    <div class="contact-phone">555 010 2847</div>
    <div class="contact-row">
      <svg width="26" height="18" viewBox="0 0 26 18"><rect x="1" y="1" width="24" height="16" fill="none" stroke="#ffc914" stroke-width="1.6"/><polyline points="1,1 13,10 25,1" fill="none" stroke="#ffc914" stroke-width="1.6"/><line x1="1" y1="17" x2="10" y2="8" stroke="#ffc914" stroke-width="1.6"/><line x1="25" y1="17" x2="16" y2="8" stroke="#ffc914" stroke-width="1.6"/></svg>
      <span>contact@solare.org</span>
      <span class="gap"></span>
      <svg width="22" height="22" viewBox="0 0 22 22" fill="none" stroke="#ffc914" stroke-width="1.6"><circle cx="11" cy="11" r="9.5"/><ellipse cx="11" cy="11" rx="4.5" ry="9.5"/><line x1="1.5" y1="11" x2="20.5" y2="11"/><line x1="3" y1="6" x2="19" y2="6"/><line x1="3" y1="16" x2="19" y2="16"/></svg>
      <span>www.solare.org</span>
    </div>
  </section>

  <section class="venue">
    <svg class="venue-pin" width="22" height="34" viewBox="0 0 22 34"><path d="M11 1C5.5 1 1 5.4 1 11c0 7.5 10 22 10 22s10-14.5 10-22C21 5.4 16.5 1 11 1z" fill="#111"/><circle cx="11" cy="11" r="4.5" fill="#ffc914"/></svg>
    <div class="venue-name">THE BROOKFIELD PERFORMING ARTS CENTER</div>
    <div class="venue-address">218 Millbrook Street Brookfield, Maine 04010</div>
  </section>
</main>
</body>
</html>
```